Steel Company / Iron Railing Business Card Template

We are a custom steel fabrication company located in Corwin Falls, OR. In business since 1979, we recently developed a new logo, and we're looking for a business card design to help display the new logo and our business. The name of the company is Kelbrook Forge Co.. The Office Phone number is (555) 555-0143. We fabricate and install custom "wrought iron" railings on our residential side, we also fabricate and erect structural steel (think cranes and steel beams in buildings) on our commercial side. Looking to get a business card template designed. Something modern, but professional. Clear and easy to read. Front should have all business and employee information including phone number(s), email address, business information, etc. back should spotlight logo.

Industry/Entity Type

Construction / Home Improvement

Contact Information for Business Card

Business information is Kelbrook Forge Co., 48 Dunmore Ave Suite 3305, Corwin Falls, OR 19074. Phone number is (555) 555-0143. Website is www.kelbrookforge.example Business card should be for "Tom Pelling" with the job title "Sales & Estimating" but be editable for other employees. Tom's phone number is (610) 555-0178

Colors

Designer to choose colors to be used in the design.

Requirements
Must have
• Modern Feel, Design should be sized for standard business card sizing 3.5" x 2" (88.9mm x 50.8mm)

```html
<!DOCTYPE html>
<html lang="en">
<head>
<meta charset="utf-8">
<title>Kelbrook Forge Co. – Business Card</title>
<link href="https://fonts.googleapis.com/css2?family=Montserrat:wght@500;600;700;800&display=swap" rel="stylesheet">
<style>
  :root {
    --navy: #1e3794;
    --navy-deep: #18307f;
    --card-blue: #2140a6;
    --red: #d9232f;
    --paper: #ffffff;
    --backdrop: #e9eaee;
    --flourish: rgba(30, 55, 148, 0.28);
  }
  * { box-sizing: border-box; margin: 0; padding: 0; }
  html, body { width: 1200px; height: 901px; overflow: hidden; }
  body {
    background: var(--backdrop);
    font-family: "Montserrat", sans-serif;
    display: flex;
    flex-direction: column;
    align-items: center;
    justify-content: center;
    gap: 46px;
  }
  .card {
    width: 630px;
    height: 360px;
    border-radius: 18px;
    position: relative;
    box-shadow: 0 10px 28px rgba(20, 30, 70, 0.18);
    overflow: hidden;
    border-bottom: 3px solid var(--red);
  }
  .card--front { background: var(--paper); }
  .card--back {
    background: var(--card-blue);
    display: flex;
    align-items: center;
    justify-content: center;
  }
  .contact {
    position: absolute;
    left: 52px;
    top: 58px;
    width: 300px;
  }
  .flourish {
    display: block;
    height: 14px;
    width: 190px;
    border-radius: 7px;
    background: var(--flourish);
  }
  .flourish--top { margin-bottom: 12px; }
  .flourish--bottom { margin-top: 12px; }
  .name {
    color: var(--navy);
    font-weight: 800;
    font-size: 25px;
    line-height: 1.1;
  }
  .job-title {
    color: var(--red);
    font-weight: 600;
    font-size: 15px;
    margin-top: 2px;
  }
  .divider {
    width: 22px;
    height: 3px;
    background: var(--red);
    margin: 9px 0 7px;
  }
  .company {
    color: var(--red);
    font-weight: 700;
    font-size: 15px;
  }
  .address {
    color: var(--navy);
    font-weight: 500;
    font-size: 14px;
    line-height: 1.4;
    font-style: normal;
  }
  .channels { list-style: none; }
  .channels li {
    display: flex;
    align-items: center;
    gap: 10px;
    color: var(--navy);
    font-weight: 500;
    font-size: 14px;
    line-height: 1.55;
  }
  .channels svg { width: 15px; height: 15px; flex: none; }
  .brand {
    position: absolute;
    right: 40px;
    top: 100px;
    width: 250px;
    display: flex;
    flex-direction: column;
    gap: 22px;
  }
  .brand__mark {
    display: flex;
    align-items: center;
    gap: 12px;
  }
  .brand__dot {
    width: 34px; height: 34px;
    border-radius: 50%;
    background: var(--red);
    flex: none;
  }
  .brand__name {
    color: var(--navy);
    font-weight: 800;
    font-size: 30px;
    line-height: 1.1;
  }
  .brand__est {
    color: var(--navy);
    font-weight: 700;
    font-size: 14px;
    letter-spacing: 3px;
    padding-left: 46px;
  }
  .back-brand {
    display: flex;
    align-items: center;
    gap: 18px;
  }
  .back-brand__dot {
    width: 54px; height: 54px;
    border-radius: 50%;
    background: var(--navy-deep);
    flex: none;
  }
  .back-brand__name {
    color: var(--navy-deep);
    font-weight: 800;
    font-size: 46px;
    line-height: 1.05;
  }
</style>
</head>
<body>
  <section class="card card--front" aria-label="Card front">
    <div class="contact">
      <span class="flourish flourish--top" role="img" aria-label="Decorative scroll flourish"></span>
      <h1 class="name">Tom Pelling</h1>
      <p class="job-title">Sales &amp; Estimating</p>
      <div class="divider"></div>
      <p class="company">Kelbrook Forge Co.</p>
      <address class="address">48 Dunmore Ave Suite 3305<br>Corwin Falls, OR 19074</address>
      <div class="divider"></div>
      <ul class="channels">
        <li>
          <svg viewBox="0 0 16 16"><circle cx="8" cy="8" r="8" fill="#d9232f"/><path d="M5 4.5l1.6-.3.8 2-1 .8a5 5 0 002.6 2.6l.8-1 2 .8-.3 1.6c-3.6.3-6.8-2.9-6.5-6.5z" fill="#fff"/></svg>
          (555) 555-0143
        </li>
        <li>
          <svg viewBox="0 0 16 16"><rect x="1" y="3" width="14" height="10" rx="1" fill="none" stroke="#d9232f" stroke-width="1.6"/><path d="M1.5 3.8L8 9l6.5-5.2" fill="none" stroke="#d9232f" stroke-width="1.6"/></svg>
          info@kelbrookforge.example
        </li>
        <li>
          <svg viewBox="0 0 16 16"><circle cx="8" cy="8" r="7.2" fill="#d9232f"/><path d="M1 8h14M8 1c-3 3-3 11 0 14M8 1c3 3 3 11 0 14" fill="none" stroke="#fff" stroke-width="1.1"/></svg>
          www.kelbrookforge.example
        </li>
      </ul>
      <span class="flourish flourish--bottom" role="img" aria-label="Decorative scroll flourish"></span>
    </div>
    <div class="brand">
      <div class="brand__mark">
        <span class="brand__dot"></span>
        <span class="brand__name">Kelbrook<br>Forge Co.</span>
      </div>
      <p class="brand__est">EST. 1979</p>
    </div>
  </section>

  <section class="card card--back" aria-label="Card back">
    <div class="back-brand">
      <span class="back-brand__dot"></span>
      <span class="back-brand__name">Kelbrook<br>Forge Co.</span>
    </div>
  </section>
</body>
</html>
```